Corvel Lane

Small ageny public transit advocacy, funding and compliance.
Consulting and lobbying efforts for small public transit agencies and communities exploring public transit opportunities.
Updates

I was interested in a simple line sketch suggesting motion, mobility. The card will be black on white. I would like it to include the bUs ones brief; Advocacy, Funding , and Compliance for small transit agencies.

Reason: I have been traveling and have had limited time to respond. Thank you all for your submit talks.

Industry/Entity Type

Consulting

Contact Information for Business Card

Mark D Loyer
Phone (614) 380-2917
Email markdloyer@vantomail.test

```html
<!DOCTYPE html>
<html lang="en">
<head>
<meta charset="utf-8">
<title>Corvel Lane — Business Cards</title>
<link rel="stylesheet" href="https://fonts.googleapis.com/css2?family=Open+Sans:wght@400;600;700&display=swap">
<style>
  :root {
    --backdrop: #bbbcbe;
    --card: #ffffff;
    --brand-blue: #283891;
    --brand-black: #000000;
    --muted: #6d6e71;
    --on-band: #ffffff;
  }
  * { margin: 0; padding: 0; box-sizing: border-box; }
  html, body {
    width: 1200px;
    height: 1000px;
    overflow: hidden;
    background: var(--backdrop);
    font-family: "Open Sans", Arial, sans-serif;
  }
  .canvas { position: relative; width: 1200px; height: 1000px; }

  .card {
    position: absolute;
    width: 602px;
    height: 340px;
    background: var(--card);
    overflow: hidden;
  }
  .card--blue  { left: 18px;  top: 17px;  --accent: var(--brand-blue); }
  .card--black { left: 576px; top: 170px; --accent: var(--brand-black); }

  .card__band { position: absolute; left: 0; top: 0; width: 602px; height: 160px; }
  .card__band path { fill: var(--accent); }

  .brand {
    position: absolute;
    left: 0; right: 0;
    top: 30px;
    text-align: center;
    color: var(--on-band);
  }
  .brand__name {
    font-weight: 700;
    font-size: 50px;
    line-height: 1;
    letter-spacing: 1px;
    text-transform: uppercase;
  }
  .brand__tagline {
    margin-top: 12px;
    font-weight: 600;
    font-size: 11.5px;
    letter-spacing: 2.2px;
  }

  .person {
    position: absolute;
    left: 50px;
    top: 253px;
  }
  .person__name {
    font-weight: 600;
    font-size: 24px;
    letter-spacing: 1.5px;
    color: var(--accent);
    line-height: 1.2;
  }
  .person__role {
    font-size: 12.5px;
    letter-spacing: 1px;
    color: var(--muted);
    text-transform: uppercase;
  }

  .contact {
    position: absolute;
    right: 60px;
    top: 256px;
    text-align: right;
    font-size: 13px;
    letter-spacing: 0.5px;
    line-height: 25px;
    color: var(--accent);
  }
  .contact__label { color: var(--muted); }
</style>
</head>
<body>
<main class="canvas">

  <article class="card card--blue">
    <svg class="card__band" viewBox="0 0 602 160" aria-hidden="true">
      <path d="M0 0 H602 V115 Q301 183 0 115 Z"/>
    </svg>
    <header class="brand">
      <div class="brand__name">Corvel Lane</div>
      <div class="brand__tagline">PUBLIC TRANSIT ADVOCACY,FUNDING AND COMPLIANCE.</div>
    </header>
    <div class="person">
      <div class="person__name">Mark D Loyer</div>
      <div class="person__role">Director</div>
    </div>
    <div class="contact">
      <div>(614) 380-2917 <span class="contact__label">(phone)</span></div>
      <div>markdloyer@vantomail.test <span class="contact__label">(e-mail)</span></div>
    </div>
  </article>

  <article class="card card--black">
    <svg class="card__band" viewBox="0 0 602 160" aria-hidden="true">
      <path d="M0 0 H602 V115 Q301 183 0 115 Z"/>
    </svg>
    <header class="brand">
      <div class="brand__name">Corvel Lane</div>
      <div class="brand__tagline">PUBLIC TRANSIT ADVOCACY,FUNDING AND COMPLIANCE.</div>
    </header>
    <div class="person">
      <div class="person__name">Mark D Loyer</div>
      <div class="person__role">Director</div>
    </div>
    <div class="contact">
      <div>(614) 380-2917 <span class="contact__label">(phone)</span></div>
      <div>markdloyer@vantomail.test <span class="contact__label">(e-mail)</span></div>
    </div>
  </article>

</main>
</body>
</html>
```